Harbour Wing Flights business card

I need a business card designed based on our logo -- designed by Studio Flock designers.

The logo is to be taken from our web site at www.harbourwingflights.com.au

I need to have this card designed quickly as its needed for business meetings
Updates

Hi Designers, Please see my updated brief for my business card. I have attached logo images and a brochure for inspiration... Regards, Gavin Trelford Harbour Wing Flights

Target Market(s)

Hotel owners and operators (concierge) and tourists to Australia

Industry/Entity Type

Business

Font styles to use
Sans Serif

Colors
84abd2
3176b5
85abd2
cedeec

Requirements
Must have
• Utilise our logo. Found on our web page www.harbourwingflights.com.au

SIDE 1
Must have my name: Gavin Trelford
Title:Owner
Phone number: 1300 418 396
Mobile:0461273958

SIDE 2
LOGO
PREPARE TO BE AMAZED! (see attached brochure for information and font style)
Nice to have
• Something that reflects aviation and tour with a light aircraft

```html
<!DOCTYPE html>
<html lang="en">
<head>
<meta charset="utf-8">
<title>Harbour Wing Flights – Business Card</title>
<link rel="stylesheet" href="https://fonts.googleapis.com/css2?family=Exo+2:wght@400;500;600&display=swap">
<style>
  :root {
    --page-bg: #e9ecf0;
    --card-bg: #ffffff;
    --brand-blue: #3176b5;
    --brand-blue-light: #84abd2;
    --brand-blue-pale: #cedeec;
    --swoosh-grey: #4b4b50;
    --ink: #2b2b33;
    --ink-soft: #55555f;
    --on-blue: #ffffff;
  }
  * { box-sizing: border-box; margin: 0; padding: 0; }
  html, body {
    width: 1057px; height: 1200px; overflow: hidden;
    background: var(--page-bg);
    font-family: "Exo 2", sans-serif;
  }
  .sheet {
    position: relative; width: 1057px; height: 1200px;
    display: flex; justify-content: center; align-items: center; gap: 60px;
  }
  .card {
    position: relative; width: 440px; height: 740px;
    background: var(--card-bg);
    box-shadow: 0 10px 30px rgba(0,0,0,.18);
    overflow: hidden;
  }
  .brand {
    position: absolute; display: flex; align-items: center; gap: 10px;
    color: var(--brand-blue); font-weight: 600; letter-spacing: .08em;
    text-transform: uppercase;
  }
  .brand-mark { width: 14px; height: 14px; background: var(--brand-blue); flex: none; }
  .card-front .brand { top: 70px; right: 40px; font-size: 19px; }
  .card-back .brand { top: 300px; left: 0; right: 0; justify-content: center; font-size: 22px; }
  .tagline {
    position: absolute; top: 344px; left: 0; right: 0; text-align: center;
    color: var(--swoosh-grey); font-size: 15px; font-weight: 500; letter-spacing: .18em;
  }

  .contact-list {
    position: absolute; top: 170px; left: 40px; list-style: none;
    color: var(--ink-soft); font-size: 15px;
  }
  .contact-address { font-size: 19px; line-height: 1.3; color: var(--ink); margin-bottom: 14px; }
  .contact-item { display: flex; align-items: center; gap: 10px; height: 30px; }
  .contact-icon { width: 20px; height: 20px; flex: none; }

  .band { position: absolute; left: 0; bottom: 0; width: 440px; height: 230px; }
  .band svg { display: block; width: 100%; height: 100%; }
  .holder {
    position: absolute; right: 34px; bottom: 44px; text-align: right;
    color: var(--on-blue); text-transform: uppercase; letter-spacing: .08em;
  }
  .holder-name { font-size: 28px; font-weight: 500; }
  .holder-title { font-size: 18px; margin-top: 4px; }
  .band-web {
    position: absolute; right: 34px; bottom: 50px;
    color: var(--on-blue); font-size: 17px; letter-spacing: .03em;
  }
</style>
</head>
<body>
<main class="sheet">

  <section class="card card-front" aria-label="Card front">
    <div class="brand"><span class="brand-mark"></span>Harbour Wing Flights</div>

    <ul class="contact-list">
      <li class="contact-address">27 Quayside Road<br>2nd Floor Pier Lane</li>
      <li class="contact-item">
        <svg class="contact-icon" viewBox="0 0 20 20"><rect width="20" height="20" rx="4" fill="var(--brand-blue)"/><path d="M6 4.5c1 0 1.6 2.2 1.4 2.8L6.6 8.2c.8 1.8 2.2 3.2 4 4l.9-.8c.6-.2 2.8.4 2.8 1.4v1.4c0 .6-.5 1.1-1.1 1.1C8.4 15.3 4.7 11.6 4.7 6.8c0-.6.5-1.1 1.1-1.1z" fill="#fff"/></svg>
        1300 418 396
      </li>
      <li class="contact-item">
        <svg class="contact-icon" viewBox="0 0 20 20"><rect width="20" height="20" rx="4" fill="var(--brand-blue)"/><rect x="5" y="8" width="10" height="7" rx="1" fill="#fff"/><rect x="7" y="4.5" width="6" height="4" fill="#fff"/></svg>
        020 418 3960
      </li>
      <li class="contact-item">
        <svg class="contact-icon" viewBox="0 0 20 20"><rect width="20" height="20" rx="4" fill="var(--brand-blue)"/><rect x="7" y="4" width="6" height="12" rx="1.2" fill="#fff"/></svg>
        0461273958
      </li>
      <li class="contact-item">
        <svg class="contact-icon" viewBox="0 0 20 20"><rect width="20" height="20" rx="4" fill="var(--brand-blue)"/><rect x="4.5" y="6" width="11" height="8" fill="#fff"/><path d="M4.5 6l5.5 4.5L15.5 6" fill="none" stroke="var(--brand-blue)" stroke-width="1.2"/></svg>
        hello@harbourwing.com
      </li>
      <li class="contact-item">
        <svg class="contact-icon" viewBox="0 0 20 20"><rect width="20" height="20" rx="4" fill="var(--brand-blue)"/><circle cx="10" cy="10" r="5.5" fill="none" stroke="#fff" stroke-width="1.3"/><path d="M4.5 10h11M10 4.5c-2.5 3-2.5 8 0 11M10 4.5c2.5 3 2.5 8 0 11" fill="none" stroke="#fff" stroke-width="1.1"/></svg>
        www.harbourwingflights.com.au
      </li>
    </ul>

    <div class="band">
      <svg viewBox="0 0 440 230" preserveAspectRatio="none" aria-hidden="true">
        <path d="M0 10 Q240 -10 440 120 L440 230 L0 230 Z" fill="var(--swoosh-grey)"/>
        <path d="M0 48 Q250 20 440 150 L440 230 L0 230 Z" fill="var(--brand-blue-pale)"/>
        <path d="M0 54 Q250 28 440 158 L440 230 L0 230 Z" fill="var(--brand-blue-light)"/>
        <path d="M0 70 Q260 50 440 175 L440 230 L0 230 Z" fill="var(--brand-blue)"/>
        <path d="M40 76 Q250 38 440 168 L440 230 Q300 80 40 76 Z" fill="var(--brand-blue)"/>
      </svg>
      <div class="holder">
        <p class="holder-name">Gavin Trelford</p>
        <p class="holder-title">Owner</p>
      </div>
    </div>
  </section>

  <section class="card card-back" aria-label="Card back">
    <div class="brand"><span class="brand-mark"></span>Harbour Wing Flights</div>
    <p class="tagline">PREPARE TO BE AMAZED!</p>
    <div class="band">
      <svg viewBox="0 0 440 230" preserveAspectRatio="none" aria-hidden="true">
        <path d="M0 10 Q240 -10 440 120 L440 230 L0 230 Z" fill="var(--swoosh-grey)"/>
        <path d="M0 48 Q250 20 440 150 L440 230 L0 230 Z" fill="var(--brand-blue-pale)"/>
        <path d="M0 54 Q250 28 440 158 L440 230 L0 230 Z" fill="var(--brand-blue-light)"/>
        <path d="M0 70 Q260 50 440 175 L440 230 L0 230 Z" fill="var(--brand-blue)"/>
        <path d="M40 76 Q250 38 440 168 L440 230 Q300 80 40 76 Z" fill="var(--brand-blue)"/>
      </svg>
      <p class="band-web">www.harbourwingflights.com.au</p>
    </div>
  </section>

</main>
</body>
</html>
```